Hexagon Honey Bottle Design, simple and elegant.

Bottle description:
BODY HEIGHT With cap 8.75cm
Without cap 8.6cm
DIAMETER Inner 4.4cm
Outer 5.2cm
Label height only has to be = 6cm height x (3.4X6) length of one hexagonal box is 3.4cm
See through bottle with black cap.
Concept of design:
Elegant, Simple, no pictures of bees, pictures of honeycomb, wooden honey stick, or drooling honey from either is ok. Simple colors. (Designer's discretion)
Wordings:
Hex1
Product of Yemen
Header:
KORVAL /MELO/ (Brand name)
Explanatory below header
Yemen Sidr Honey from The Valley Ra'ufil (100% Pure)
(name of honey)
250g
Optional
Hex2
Pure
=
No Additives (not even natural additives)
Hex3
Raw
=
Unheated, Unpasteurized, Unprocessed honey
Hex4
Natural
=
No added color, artificial flavor, or synthetic substance
Hex5
RENOWNED
=
Very well known by honey lovers
(Natural Pure Raw and Renowned) wordings to be on a suitable place on the bottle (maybe on the cap) -
Hex6
Imported By
The Lantern Bazaar Pte Ltd
No. 317, Cobalt Ferry Road, #09-12
Cobalt Ferry Plaza
Singapore 195340
Wordings can be rearranged - its up to the designer's discretion where and how to place them and in which order.-
Designer must be willing to do numerous changes as the design develops

```html
<!DOCTYPE html>
<html lang="en">
<head>
<meta charset="utf-8">
<title>KORVAL MELO – Hexagon Honey Jar Labels</title>
<link href="https://fonts.googleapis.com/css2?family=Oswald:wght@300&family=Open+Sans:wght@400;700&family=Libre+Baskerville&family=Kaushan+Script&family=Nunito:wght@800&display=swap" rel="stylesheet">
<style>
  :root {
    --bg: #ffffff;
    --ink: #111111;
    --orange: #f5a00c;
    --brown: #2a1c0c;
    --gold: #f4b400;
    --gold-light: #ffd84a;
    --cream: #fde48b;
    --cream-icon: #efcf6a;
    --panel-text: #3a2d1c;
    --cap: #050505;
    --white: #ffffff;
  }
  * { box-sizing: border-box; margin: 0; padding: 0; }
  html, body { width: 1200px; height: 826px; overflow: hidden; background: var(--bg); }
  .canvas { position: relative; width: 1200px; height: 826px; font-family: "Open Sans", sans-serif; }

  .view-title {
    position: absolute; top: 120px; width: 200px; text-align: center;
    font-family: "Nunito", sans-serif; font-weight: 800; font-size: 35px; color: var(--ink);
  }
  .view-title--front { left: 204px; }
  .view-title--back { left: 802px; }

  /* Cap lid */
  .cap {
    position: absolute; left: 469px; top: 22px; width: 242px; height: 242px; border-radius: 50%;
    background: radial-gradient(circle at 45% 40%, #1c1c1c 0%, var(--cap) 70%);
    display: flex; flex-direction: column; align-items: center; padding-top: 50px;
    color: var(--gold);
  }
  .cap__claims { font-family: "Oswald", sans-serif; font-weight: 300; font-size: 15px; line-height: 20px; text-align: center; letter-spacing: .5px; }
  .cap__rule { width: 104px; height: 1px; background: var(--gold); margin: 6px 0 8px; }
  .cap__dot { width: 18px; height: 18px; border-radius: 50%; background: var(--gold); }
  .cap__brand {
    font-family: "Open Sans", sans-serif; font-weight: 400; font-size: 13px; letter-spacing: 1px;
    color: var(--gold); margin-top: 6px;
  }

  /* Side claim panels */
  .claim-panel {
    position: absolute; top: 300px; width: 137px; height: 211px; border-radius: 13px;
    background: var(--cream); text-align: center; color: var(--panel-text);
  }
  .claim-panel--raw { left: 26px; }
  .claim-panel--pure { left: 449px; }
  .claim-panel--natural { left: 619px; }
  .claim-panel--renowned { left: 1042px; }
  .claim-panel__art {
    width: 90px; height: 80px; margin: 18px auto 0; border-radius: 50%;
    background: radial-gradient(circle, var(--cream-icon) 0%, var(--cream) 75%);
  }
  .claim-panel__word { font-family: "Kaushan Script", cursive; font-size: 31px; line-height: 36px; margin-top: 14px; color: #2a2218; }
  .claim-panel--renowned .claim-panel__word { font-size: 25px; }
  .claim-panel__note { font-size: 8.5px; line-height: 11px; }
  .claim-panel__note strong { font-size: 11px; display: block; }
  .claim-panel__note em { font-style: normal; color: #6a5a3a; }

  /* Jar label */
  .jar-label {
    position: absolute; top: 318px; width: 138px; height: 211px; border-radius: 12px; overflow: hidden;
    background: var(--brown); display: flex; flex-direction: column;
  }
  .jar-label--front { left: 238px; }
  .jar-label--back { left: 832px; }
  .jar-label__origin {
    height: 27px; background: var(--orange); color: var(--white);
    font-size: 10.5px; line-height: 27px; text-align: center;
  }
  .jar-label__masthead {
    height: 78px; display: flex; flex-direction: column; align-items: center;
    padding-top: 14px; position: relative;
  }
  .jar-label__masthead::before, .jar-label__masthead::after {
    content: ""; position: absolute; left: 0; right: 0; height: 1px; background: var(--gold);
  }
  .jar-label__masthead::before { top: 4px; }
  .jar-label__masthead::after { bottom: 4px; }
  .jar-label__dot { width: 20px; height: 20px; border-radius: 50%; background: var(--gold); }
  .jar-label__brand {
    font-family: "Open Sans", sans-serif; font-weight: 400; font-size: 13px; letter-spacing: 1px;
    line-height: 18px; color: var(--gold-light); margin-top: 8px;
  }
  .jar-label__body {
    flex: 1; background: linear-gradient(180deg, var(--orange) 0%, var(--gold) 45%, var(--gold-light) 100%);
    border-radius: 0 0 14px 14px; text-align: center; color: var(--panel-text); padding-top: 8px;
  }
  .jar-label__honey { font-size: 6.5px; line-height: 9px; color: #5a3f14; }
  .jar-label__claims { font-family: "Libre Baskerville", serif; font-size: 13px; line-height: 15px; color: var(--brown); margin-top: 6px; }
  .jar-label__weight { height: 27px; color: var(--white); font-size: 9.5px; line-height: 27px; text-align: center; }
  .jar-label__importer { font-size: 6.5px; line-height: 9px; color: #4a3614; }
  .jar-label__importer strong { color: var(--brown); }
  .jar-label__code {
    width: 100px; height: 32px; margin: 9px auto 0; background: var(--white);
    font-size: 8px; font-weight: 700; line-height: 32px; color: var(--ink);
  }
  .jar-label--back .jar-label__body { border-radius: 0; }
</style>
</head>
<body>
<main class="canvas">

  <h2 class="view-title view-title--front">front</h2>
  <h2 class="view-title view-title--back">back</h2>

  <section class="cap" aria-label="Jar cap">
    <p class="cap__claims">RAW<br>PURE<br>NATURAL<br>RENOWNED</p>
    <span class="cap__rule"></span>
    <span class="cap__dot"></span>
    <p class="cap__brand">KORVAL MELO</p>
  </section>

  <article class="claim-panel claim-panel--raw">
    <div class="claim-panel__art" role="img" aria-label="Faint round raw stamp illustration"></div>
    <h3 class="claim-panel__word">Raw</h3>
    <p class="claim-panel__note">Unheated,<br>Unpasteurized,<br>Unprocessed honey</p>
  </article>

  <article class="jar-label jar-label--front">
    <p class="jar-label__origin">Product of Yemen</p>
    <div class="jar-label__masthead">
      <span class="jar-label__dot"></span>
      <p class="jar-label__brand">KORVAL MELO</p>
    </div>
    <div class="jar-label__body">
      <p class="jar-label__honey">Yemen Sidr Honey<br>from The Valley Ra'ufil<br>(100% Pure)</p>
      <p class="jar-label__claims">NATURAL<br>PURE RAW</p>
    </div>
    <p class="jar-label__weight">250g</p>
  </article>

  <article class="claim-panel claim-panel--pure">
    <div class="claim-panel__art" role="img" aria-label="Faint honeycomb cells with honey drop illustration"></div>
    <h3 class="claim-panel__word">Pure</h3>
    <p class="claim-panel__note"><strong>No Additives</strong><em>(not even natural additives)</em></p>
  </article>

  <article class="claim-panel claim-panel--natural">
    <div class="claim-panel__art" role="img" aria-label="Faint leaf illustration"></div>
    <h3 class="claim-panel__word">Natural</h3>
    <p class="claim-panel__note">No added color,<br>artificial flavor,<br>or synthetic substance</p>
  </article>

  <article class="jar-label jar-label--back">
    <p class="jar-label__origin">Product of Yemen</p>
    <div class="jar-label__masthead">
      <span class="jar-label__dot"></span>
      <p class="jar-label__brand">KORVAL MELO</p>
    </div>
    <div class="jar-label__body">
      <p class="jar-label__importer">Imported By<br><strong>The Lantern Bazaar Pte Ltd</strong><br>No. 317, Cobalt Ferry Road, #09-12<br>Cobalt Ferry Plaza<br>Singapore 195340</p>
      <p class="jar-label__code">barcode area</p>
    </div>
  </article>

  <article class="claim-panel claim-panel--renowned">
    <div class="claim-panel__art" role="img" aria-label="Faint burst of honey drops illustration"></div>
    <h3 class="claim-panel__word">Renowned</h3>
    <p class="claim-panel__note">Very well known<br>by honey lovers</p>
  </article>

</main>
</body>
</html>
```